BRAVEN WALLCOTE Business Card Design (logo attached)

Supply and installation of home insulation for residential and commercial properties.
Eco friendly because the products are used from recycled materials but also helps reduce energy consumption such as electricity and gas to cool and heat the building.
We have been in the building industry for 15years.
our website to have a look at is www.bravenwallcote.com.au

I would like the cards to be modern, fresh with warm colors like grey, greens, blue that works with the grey. The logo is attached and I am happy to change the shade of green to match the new card. I
I have a previous b-card (see attached) but am interested in a completely new design ideas.
You need to keep the symbol but can change the font.
Updates

The card does not need to have the ABN and ACN details. Also if you need to remove any logos you can take out the Stone Mark one. Thanks! Please dont use black

Reason: There is a completely new design and designer that has displayed a b-card and I would really like to see whether to go with the new design and concept or keep it standard. Regards Norah

Here are my full details to add to the cards please. Name: Gordon Pellish - Managing Director Phone: (08) 9461 3850 Mobile: 0417 586 209 Email: info@bravenwallcote.com.au Web: www.bravenwallcote.com.au Postal: PO Box 7318, Kelbury WA 6920

Industry/Entity Type

Residential

Requirements
Must have
• QRT Logo / DWL Logo
Insulation Products Logo
Need to keep the symbol but can change the font
Should not have
• Do not use black even for the text
Does not need the faded green from the previous cards

```html
<!DOCTYPE html>
<html lang="en">
<head>
<meta charset="utf-8">
<title>Braven Wallcote Business Card</title>
<link rel="stylesheet" href="https://fonts.googleapis.com/css2?family=Open+Sans:ital,wght@0,400;0,600;0,700;1,600&display=swap">
<style>
  :root {
    --backdrop: #e8e8e8;
    --paper: #ffffff;
    --green-deep: #0f7a35;
    --green-mid: #2f9b2a;
    --green-bright: #7cc520;
    --green-lime: #a6d93a;
    --green-text: #1f8a3a;
    --badge-blue: #2c6fb6;
    --badge-teal: #2f8f6f;
    --badge-pink: #e2388f;
    --badge-orange: #ef7d22;
    --badge-gold: #d9b21f;
    --badge-green: #1e7a3c;
    --white: #ffffff;
  }
  * { margin: 0; padding: 0; box-sizing: border-box; }
  html, body { width: 1200px; height: 848px; overflow: hidden; }
  body {
    background: var(--backdrop);
    font-family: "Open Sans", Arial, sans-serif;
    position: relative;
  }
  .card {
    position: absolute;
    top: 266px;
    width: 520px;
    height: 316px;
    background: var(--paper);
    box-shadow: 0 6px 18px rgba(60, 60, 60, 0.18);
    overflow: hidden;
  }
  .card--front { left: 60px; }
  .card--back { left: 620px; }
  .card__art { position: absolute; inset: 0; width: 100%; height: 100%; }

  .brand {
    position: absolute;
    display: flex;
    align-items: center;
    gap: 8px;
    font-weight: 700;
    font-size: 19px;
    letter-spacing: 0.5px;
    color: var(--green-text);
  }
  .brand__dot {
    width: 14px; height: 14px; border-radius: 50%;
    background: var(--green-bright);
  }
  .card--front .brand { left: 40px; top: 242px; }
  .card--back .brand { left: 30px; top: 92px; font-size: 17px; }

  .services {
    position: absolute;
    right: 40px; top: 40px;
    text-align: right;
    color: var(--white);
    font-weight: 600;
    font-size: 13px;
    line-height: 1.35;
    letter-spacing: 0.4px;
    text-transform: uppercase;
  }

  .contact {
    position: absolute;
    left: 30px; top: 168px;
    color: var(--white);
  }
  .contact__name { font-weight: 700; font-size: 19px; letter-spacing: 0.5px; text-transform: uppercase; }
  .contact__role { font-weight: 600; font-style: italic; font-size: 13px; color: var(--green-lime); margin-bottom: 4px; }
  .contact__line { display: flex; align-items: center; gap: 6px; font-size: 12.5px; font-weight: 600; line-height: 1.45; }
  .icon {
    width: 13px; height: 13px; border-radius: 50%;
    background: var(--green-lime);
    display: inline-flex; align-items: center; justify-content: center;
    flex-shrink: 0;
  }
  .icon svg { width: 9px; height: 9px; }

  .website {
    position: absolute;
    left: 0; right: 0; bottom: 8px;
    text-align: center;
    color: var(--green-lime);
    font-weight: 700;
    font-size: 13px;
    letter-spacing: 5px;
    text-transform: uppercase;
  }

  .partners { position: absolute; inset: 0; }
  .partner { position: absolute; border-radius: 4px; }
  .partner--blue { left: 282px; top: 70px; width: 70px; height: 24px; background: var(--badge-blue); }
  .partner--teal { left: 358px; top: 50px; width: 66px; height: 24px; background: var(--badge-teal); border-radius: 12px; }
  .partner--pink { left: 282px; top: 104px; width: 82px; height: 24px; background: var(--badge-pink); }
  .partner--orange { left: 290px; top: 138px; width: 86px; height: 22px; background: var(--badge-orange); }
  .partner--gold { left: 378px; top: 90px; width: 26px; height: 26px; background: var(--badge-gold); border-radius: 50%; }
  .partner--green { left: 436px; top: 14px; width: 34px; height: 40px; background: var(--badge-green); }
  .partner--blue-sq { left: 470px; top: 62px; width: 30px; height: 30px; background: var(--badge-blue); }
  .partner-name {
    position: absolute; left: 370px; top: 120px;
    font-size: 10px; font-weight: 600; color: var(--green-text);
  }
</style>
</head>
<body>

  <!-- Front of card -->
  <section class="card card--front">
    <svg class="card__art" viewBox="0 0 520 316" aria-hidden="true">
      <defs>
        <linearGradient id="frontGreen" x1="0" y1="0" x2="1" y2="1">
          <stop offset="0" stop-color="#8fcf2a"/>
          <stop offset="0.55" stop-color="#4fae24"/>
          <stop offset="1" stop-color="#1f8a2f"/>
        </linearGradient>
      </defs>
      <path d="M0 0 H520 V180 C420 150 220 150 0 205 Z" fill="url(#frontGreen)"/>
      <path d="M250 0 C215 60 235 130 300 160 C260 120 250 60 290 0 Z" fill="#0f7a35" opacity="0.85"/>
      <path d="M0 205 C220 150 420 150 520 180 V196 C410 172 230 170 0 218 Z" fill="#a6d93a"/>
    </svg>
    <p class="services">Home Insulation<br>&amp; Removal<br>Gutter Mesh<br>Whirly Birds</p>
    <div class="brand"><span class="brand__dot"></span>BRAVEN WALLCOTE</div>
  </section>

  <!-- Back of card -->
  <section class="card card--back">
    <svg class="card__art" viewBox="0 0 520 316" aria-hidden="true">
      <defs>
        <linearGradient id="backGreen" x1="0" y1="0" x2="1" y2="1">
          <stop offset="0" stop-color="#7cc520"/>
          <stop offset="0.6" stop-color="#3a9f28"/>
          <stop offset="1" stop-color="#1f8a2f"/>
        </linearGradient>
      </defs>
      <rect width="520" height="316" fill="url(#backGreen)"/>
      <path d="M0 0 H250 C235 80 160 135 0 160 Z" fill="#ffffff"/>
      <path d="M520 0 V175 C440 172 330 170 270 160 C268 90 300 30 340 0 Z" fill="#ffffff"/>
      <path d="M340 0 C290 35 262 100 270 160 C250 110 268 40 310 0 Z" fill="#0f7a35"/>
      <path d="M270 160 C330 170 440 172 520 175 V190 C430 185 330 182 260 172 Z" fill="#a6d93a"/>
      <rect y="278" width="520" height="38" fill="#0f7a35"/>
    </svg>

    <div class="brand"><span class="brand__dot"></span>BRAVEN WALLCOTE</div>

    <div class="partners">
      <span class="partner partner--green" role="img" aria-label="Industry association badge"></span>
      <span class="partner partner--blue-sq" role="img" aria-label="Builders association badge"></span>
      <span class="partner partner--teal" role="img" aria-label="Insulation product badge"></span>
      <span class="partner partner--blue" role="img" aria-label="Insulation product badge"></span>
      <span class="partner partner--pink" role="img" aria-label="Insulation product badge"></span>
      <span class="partner partner--orange" role="img" aria-label="Insulation product badge"></span>
      <span class="partner partner--gold" role="img" aria-label="Gutter guard product badge"></span>
    </div>

    <div class="contact">
      <p class="contact__name">Gordon Pellish</p>
      <p class="contact__role">Project Manager</p>
      <p class="contact__line">
        <span class="icon"><svg viewBox="0 0 10 10"><path d="M2 1 L4 1 L4.6 3 L3.5 3.8 C4 5 5 6 6.2 6.5 L7 5.4 L9 6 L9 8 C5 8.5 1.5 5 2 1 Z" fill="#0f7a35"/></svg></span>
        0417 586 209 ; (08) 9461 3850
      </p>
      <p class="contact__line">
        <span class="icon"><svg viewBox="0 0 10 10"><circle cx="5" cy="5" r="2.2" fill="none" stroke="#0f7a35" stroke-width="1.4"/></svg></span>
        info@bravenwallcote.com.au
      </p>
      <p class="contact__line">
        <span class="icon"><svg viewBox="0 0 10 10"><path d="M5 1 C3 1 2 2.5 2 4 C2 6 5 9 5 9 C5 9 8 6 8 4 C8 2.5 7 1 5 1 Z" fill="#0f7a35"/></svg></span>
        PO Box 7318, Kelbury WA 6920
      </p>
    </div>

    <p class="website">www.bravenwallcote.com.au</p>
  </section>

</body>
</html>
```